Business price tag design for Furniture Business

Hello,

I have developed a tag for a home furniture business and need 1 more creative template. Please see attachment. I need the template to be very appealing.

Requirements:

1.Tag dimensions needs to be about the same as attached tag.
2. Tag design needs to be suitable for a home furniture business.
3. Tag needs to have locations for the following: Item Title, Now Price, Was Price, Product Number.
4. "The black shape at the bottom of attached tag could be removed.

I have no requirements on colors, but something professional is needed, preferably white background to reduce print ink consumption.

Please see attachment for clarification.

Industry/Entity Type

Retail

Font styles to use
Serif
Sans Serif

Requirements
Must have
• Please see Project Description.
Nice to have

```html
<!DOCTYPE html>
<html lang="en">
<head>
<meta charset="utf-8">
<title>Furniture Price Tag</title>
<link rel="stylesheet" href="https://fonts.googleapis.com/css2?family=Archivo+Black&display=swap">
<style>
  :root {
    --tag-bg: #e3e3e3;
    --tag-bg-light: #ebebeb;
    --ink-black: #111111;
    --price-red: #a6111b;
    --panel-white: #fbfbfb;
    --band-red: #cf2530;
    --band-dark: #4e0005;
    --band-text: #efe6e6;
    --dial-face: #e4e4e4;
  }
  html, body {
    margin: 0;
    padding: 0;
    width: 720px;
    height: 1200px;
    overflow: hidden;
    background: var(--tag-bg);
  }
  .price-tag {
    position: relative;
    width: 720px;
    height: 1200px;
    background: radial-gradient(ellipse at 50% 40%, var(--tag-bg-light), var(--tag-bg) 70%);
    font-family: "Archivo Black", "Arial Black", sans-serif;
  }
  .item-title {
    position: absolute;
    top: 40px;
    left: 0;
    width: 100%;
    margin: 0;
    text-align: center;
    font-size: 70px;
    line-height: 1;
    font-weight: 400;
    letter-spacing: 1px;
    color: var(--ink-black);
  }
  .price-label {
    position: absolute;
    left: 43px;
    width: 634px;
    height: 110px;
    background: var(--panel-white);
    box-shadow: 0 8px 14px rgba(0,0,0,0.28), 0 2px 4px rgba(0,0,0,0.15);
    display: flex;
    align-items: center;
    justify-content: center;
    color: var(--price-red);
    font-size: 76px;
    letter-spacing: 1px;
    line-height: 1;
  }
  .price-label--now { top: 172px; }
  .price-label--was { top: 608px; }
  .price-dial {
    position: absolute;
    left: 247px;
    width: 226px;
    height: 226px;
    border-radius: 50%;
    background: radial-gradient(circle at 40% 35%, #ededed, var(--dial-face) 60%, #dadada);
    box-shadow: 0 6px 10px rgba(0,0,0,0.35), inset 0 2px 3px rgba(255,255,255,0.8), inset 0 -3px 5px rgba(0,0,0,0.08);
  }
  .price-dial--now { top: 336px; }
  .price-dial--was { top: 770px; }
  .product-band {
    position: absolute;
    left: 0;
    top: 1037px;
    width: 100%;
    height: 92px;
    background: linear-gradient(90deg, var(--band-red) 0%, #a5161f 50%, var(--band-dark) 100%);
    display: flex;
    align-items: center;
    justify-content: center;
    color: var(--band-text);
    font-size: 50px;
    letter-spacing: 1px;
    line-height: 1;
  }
</style>
</head>
<body>
  <main class="price-tag">
    <h1 class="item-title">ITEM TITLE</h1>
    <div class="price-label price-label--now">NOW PRICE</div>
    <div class="price-dial price-dial--now"></div>
    <div class="price-label price-label--was">WAS PRICE</div>
    <div class="price-dial price-dial--was"></div>
    <div class="product-band">PRODUCT NUMBER</div>
  </main>
</body>
</html>
```